Business Card and Simple Logo Desgin

New Zealand based start up company "Brook Advisory LTD" requires business cards and simple logo design.

Card Content.

Brook Advisory LTD

Joanna Pritchard
CA, BMS (Hons)

j.pritchard@brookadvisory.co.nz
PH +64 21 574 160

Target Market(s)

Corporate Business in IT, Finance and accounting.

Industry/Entity Type

Business

```html
<!DOCTYPE html>
<html lang="en">
<head>
<meta charset="utf-8">
<title>Brook Advisory LTD – Business Card</title>
<link rel="stylesheet" href="https://fonts.googleapis.com/css2?family=Arimo:wght@400;700&display=swap">
<style>
  :root {
    --page-bg: #e9eaeb;
    --brand-blue: #1e8fdc;
    --blue-light: #6cc8f4;
    --blue-deep: #1577c9;
    --accent-green: #74c61a;
    --green-soft: #a8dd8a;
    --card-white: #ffffff;
    --text-blue: #1a7fcf;
    --font-main: "Arimo", Arial, sans-serif;
  }
  * { box-sizing: border-box; margin: 0; padding: 0; }
  html, body {
    width: 1200px;
    height: 898px;
    overflow: hidden;
    background: var(--page-bg);
    font-family: var(--font-main);
  }
  .canvas {
    width: 1200px;
    height: 898px;
    display: flex;
    flex-direction: column;
    align-items: center;
    justify-content: center;
    gap: 56px;
  }
  .card {
    position: relative;
    width: 620px;
    height: 354px;
    border-radius: 4px;
    overflow: hidden;
    box-shadow: 0 6px 18px rgba(0, 0, 0, 0.18);
  }
  .card-art {
    position: absolute;
    inset: 0;
    width: 100%;
    height: 100%;
  }

  /* Back side */
  .card-back {
    background: linear-gradient(160deg, var(--blue-light) 0%, var(--brand-blue) 55%, var(--blue-deep) 100%);
  }
  .card-back .brand {
    position: absolute;
    left: 0; right: 0;
    top: 150px;
    display: flex;
    align-items: center;
    justify-content: center;
    gap: 14px;
    color: var(--card-white);
    font-size: 30px;
    font-weight: 400;
  }
  .card-back .brand-square {
    width: 40px;
    height: 40px;
    background: var(--card-white);
  }

  /* Front side */
  .card-front { background: var(--card-white); }
  .card-front .content {
    position: absolute;
    left: 0; right: 0;
    top: 40px;
    text-align: center;
  }
  .card-front .brand {
    display: flex;
    align-items: center;
    justify-content: center;
    gap: 12px;
    color: var(--text-blue);
    font-size: 22px;
    font-weight: 400;
  }
  .card-front .brand-square {
    width: 34px;
    height: 34px;
    background: var(--brand-blue);
  }
  .person-name,
  .person-credentials {
    color: var(--accent-green);
    font-weight: 700;
    font-size: 26px;
    line-height: 1.2;
  }
  .person-name { margin-top: 26px; }
  .contact {
    margin-top: 18px;
    color: var(--text-blue);
    font-size: 14px;
    line-height: 1.35;
  }
</style>
</head>
<body>
<main class="canvas">

  <section class="card card-back" aria-label="Business card back">
    <svg class="card-art" viewBox="0 0 620 354" preserveAspectRatio="none" aria-hidden="true">
      <defs>
        <linearGradient id="sheen" x1="0" y1="0" x2="1" y2="0">
          <stop offset="0" stop-color="#ffffff" stop-opacity="0.05"/>
          <stop offset="0.5" stop-color="#ffffff" stop-opacity="0.35"/>
          <stop offset="1" stop-color="#ffffff" stop-opacity="0.05"/>
        </linearGradient>
      </defs>
      <path d="M0,120 Q310,300 620,150 L620,0 L0,0 Z" fill="url(#sheen)"/>
      <path d="M0,250 Q320,360 620,230 L620,354 L0,354 Z" fill="#0f6cb8" opacity="0.25"/>
    </svg>
    <div class="brand">
      <span class="brand-square"></span>
      <span class="brand-name">Brook Advisory LTD</span>
    </div>
  </section>

  <section class="card card-front" aria-label="Business card front">
    <svg class="card-art" viewBox="0 0 620 354" preserveAspectRatio="none" aria-hidden="true">
      <defs>
        <linearGradient id="wave-blue" x1="0" y1="0" x2="0" y2="1">
          <stop offset="0" stop-color="#4cb6ee"/>
          <stop offset="1" stop-color="#1a86d6"/>
        </linearGradient>
      </defs>
      <path d="M0,228 Q300,335 620,248 L620,354 L0,354 Z" fill="var(--green-soft)"/>
      <path d="M0,240 Q310,344 620,258 L620,354 L0,354 Z" fill="url(#wave-blue)"/>
    </svg>
    <div class="content">
      <div class="brand">
        <span class="brand-square"></span>
        <span class="brand-name">Brook Advisory LTD</span>
      </div>
      <p class="person-name">Joanna Pritchard</p>
      <p class="person-credentials">CA, BMS (Hons)</p>
      <div class="contact">
        <p class="contact-email">j.pritchard@brookadvisory.co.nz</p>
        <p class="contact-phone">PH +64 21 574 160</p>
      </div>
    </div>
  </section>

</main>
</body>
</html>
```